R7M Meridian Business Card Design

We need a business card created for our New Business "R7M Meridian"<br/><br/>The business card design is up to you however the following information must be on the business card:<br/><br/>Front of the business card -<br/>Email :dorianv@r7mmeridian.nz<br/>Mobile: +64 (0) 22 4871 659<br/>Website: www.r7mmeridian.nz<br/>Card Owner Name: Dorian Valcourt<br/>Company Title: Business Development Manager<br/>Slogan: "The BEST of both worlds". <br/>Logo On the front attached to the design brief<br/><br/>On the back: <br/>Space on the back for 4 more versions of the logo across the bottom of the card indicating different subsidiary brands - R7M Coffee, R7M Arts, R7M ?? (The card will be used for all of these brands - We Will add the extra subsidiary logos to the design once the design is finished (We are a graphics design team). <br/><br/>Other than that we want a premium feeling logo that remains universally usable depending on the business entity that we are using the card for. The use of bright bold colours would be great but we still want the card to feel premium.
Target Market(s)
Gift Design and Manufacturing Companies
Contact Information for Business Card
Front of the business card -
Email :dorianv@r7mmeridian.nz
Mobile: +64 (0) 22 4871 659
Website: www.r7mmeridian.nz
Card Owner Name: Dorian Valcourt
Company Title: Business Development Manager
Slogan: "The BEST of both worlds".
Logo On the front attached to the design brief

```html
<!DOCTYPE html>
<html lang="en">
<head>
<meta charset="utf-8">
<title>R7M Meridian – Business Card</title>
<link href="https://fonts.googleapis.com/css2?family=Open+Sans:ital,wght@0,400;0,600;0,700;1,400;1,700&display=swap" rel="stylesheet">
<style>
  :root {
    --stage: #2a2a2c;
    --card: #1c1c1e;
    --card-edge: #141416;
    --accent: #3346b0;
    --accent-bright: #4056c9;
    --ink: #f2f2f2;
    --emboss: #2c2c2f;
    --emboss-rim: #3a3a3e;
  }
  * { box-sizing: border-box; margin: 0; padding: 0; }
  html, body { width: 1200px; height: 900px; overflow: hidden; }
  body {
    background: var(--stage);
    font-family: "Open Sans", Arial, sans-serif;
    color: var(--ink);
    position: relative;
  }
  .card {
    position: absolute;
    left: 250px;
    width: 700px;
    height: 400px;
    background: var(--card);
    border: 1px solid var(--card-edge);
    box-shadow: 0 14px 30px rgba(0,0,0,.45);
    overflow: hidden;
  }
  .card--front { top: 40px; }
  .card--back { top: 460px; }

  /* Front */
  .brand {
    position: absolute;
    display: flex;
    align-items: center;
    gap: 12px;
    font-weight: 700;
    color: var(--accent-bright);
    white-space: nowrap;
  }
  .card--front .brand { left: 48px; top: 150px; font-size: 30px; }
  .brand__dot {
    width: 22px; height: 22px;
    border-radius: 50%;
    background: currentColor;
    flex: none;
  }
  .divider {
    position: absolute;
    left: 320px; top: 110px;
    width: 1.5px; height: 170px;
    background: var(--accent);
  }
  .contact-block {
    position: absolute;
    left: 346px; top: 112px;
  }
  .owner-name {
    font-weight: 700;
    font-style: italic;
    font-size: 27px;
    letter-spacing: 7px;
    text-transform: uppercase;
    color: var(--accent-bright);
    line-height: 1.1;
  }
  .owner-role {
    font-size: 17px;
    margin-top: 6px;
    margin-bottom: 14px;
  }
  .contact-list { list-style: none; }
  .contact-list li {
    display: flex;
    align-items: center;
    gap: 10px;
    font-size: 17px;
    line-height: 1.55;
  }
  .contact-list svg { width: 14px; height: 14px; flex: none; fill: var(--ink); }
  .accent { color: var(--accent-bright); }
  .slogan { font-size: 18px; font-style: italic; }
  .slogan .accent { font-style: italic; }
  .card--front .slogan { position: absolute; left: 78px; top: 300px; font-style: normal; }

  /* Back */
  .card--back .brand {
    left: 0; right: 0; top: 120px;
    justify-content: center;
    font-size: 46px;
    color: var(--emboss);
    text-shadow: none;
  }
  .card--back .brand__dot { width: 34px; height: 34px; background: var(--emboss-rim); }
  .card--back .slogan {
    position: absolute;
    left: 0; right: 0; top: 255px;
    text-align: center;
    font-style: normal;
  }
  .range-band {
    position: absolute;
    left: 200px; bottom: 0;
    width: 300px; height: 44px;
    background: var(--accent);
    display: flex;
    align-items: center;
    justify-content: center;
    font-size: 16px;
    letter-spacing: .5px;
    text-transform: uppercase;
  }
</style>
</head>
<body>

<section class="card card--front" aria-label="Business card front">
  <div class="brand"><span class="brand__dot"></span>R7M Meridian</div>
  <div class="divider"></div>
  <div class="contact-block">
    <h1 class="owner-name">Dorian Valcourt</h1>
    <p class="owner-role">Business Development Manager</p>
    <ul class="contact-list">
      <li>
        <svg viewBox="0 0 14 14" aria-hidden="true"><path d="M4 0h6a1.5 1.5 0 0 1 1.5 1.5v11A1.5 1.5 0 0 1 10 14H4a1.5 1.5 0 0 1-1.5-1.5v-11A1.5 1.5 0 0 1 4 0zm0 1.6v9.4h6V1.6zM7 11.6a.8.8 0 1 0 0 1.6.8.8 0 0 0 0-1.6z"/></svg>
        +64 (0) 22 4871 659
      </li>
      <li>
        <svg viewBox="0 0 14 14" aria-hidden="true"><path d="M0 3h14v8H0zm1.2 1 5.8 4 5.8-4z"/></svg>
        dorianv@r7mmeridian.nz
      </li>
      <li>
        <svg viewBox="0 0 14 14" aria-hidden="true"><path d="M7 0a7 7 0 1 0 0 14A7 7 0 0 0 7 0zm0 1.4c.8 0 1.7 1.8 2 4.6H5c.3-2.8 1.2-4.6 2-4.6zM1.5 7.6h2.1c.1 1.7.4 3.2.9 4.2A5.6 5.6 0 0 1 1.5 7.6zm0-1.6A5.6 5.6 0 0 1 4.5 2.2c-.5 1-.8 2.3-.9 3.8zm5.5 6.6c-.8 0-1.7-2-2-5h4c-.3 3-1.2 5-2 5zm2.5-.8c.5-1 .8-2.5.9-4.2h2.1a5.6 5.6 0 0 1-3 4.2zm.9-5.8c-.1-1.5-.4-2.8-.9-3.8a5.6 5.6 0 0 1 3 3.8z"/></svg>
        <span>www.<span class="accent">r7mmeridian</span>.nz</span>
      </li>
    </ul>
  </div>
  <p class="slogan">The <span class="accent">BEST</span> of both worlds</p>
</section>

<section class="card card--back" aria-label="Business card back">
  <div class="brand"><span class="brand__dot"></span>R7M Meridian</div>
  <p class="slogan">The <span class="accent">BEST</span> of both worlds</p>
  <div class="range-band">Gifts, Art, Coffee, ????</div>
</section>

</body>
</html>
```